Songs Cover Art. Song tittle DJ K - Turn the Lights Low

Hey

I need a cover art for my songs. My genre is Big Room House/EDM music and my DJ name is DJ K. Song title is Turn the Lights Low. I'm a producer and i need a designer to design all my cover art so that i will be able upload my song with a cover art. Do let me know if you have any questions.

Song Tittle: Turn the Lights Low
Artist name: DJ K

Thanks

Reason: I will give more time in order for you guys to create more design!

Industry/Entity Type

House

Requirements
Should not have
• Please dont make the design to colourful.

```html
<!DOCTYPE html>
<html lang="en">
<head>
<meta charset="UTF-8">
<title>DJ K – Turn the Lights Low</title>
<link rel="stylesheet" href="https://fonts.googleapis.com/css2?family=Jost:wght@600;700&display=swap">
<style>
  :root {
    --cover-black: #0b0b0b;
    --cover-charcoal: #1c1c1c;
    --silver-light: #f0f0f0;
    --silver-mid: #c9c9c9;
    --silver-dark: #9a9a9a;
    --artist-white: #ffffff;
  }
  html, body {
    margin: 0;
    padding: 0;
    width: 1200px;
    height: 1200px;
    overflow: hidden;
    background: var(--cover-black);
  }
  .cover {
    position: relative;
    width: 1200px;
    height: 1200px;
    overflow: hidden;
    font-family: "Jost", "Futura", sans-serif;
  }
  .cover__texture {
    position: absolute;
    inset: 0;
    background:
      radial-gradient(ellipse at 50% 40%, var(--cover-charcoal) 0%, #121212 45%, var(--cover-black) 100%);
  }
  .cover__frame {
    position: absolute;
    left: 104px;
    top: 112px;
    width: 960px;
    height: 958px;
    border: 8px solid var(--silver-mid);
  }
  .cover__title {
    position: absolute;
    left: 0;
    right: 0;
    top: 200px;
    margin: 0;
    text-align: center;
    font-weight: 700;
    font-size: 158px;
    line-height: 178px;
    letter-spacing: 1px;
    text-transform: uppercase;
    background: linear-gradient(160deg, var(--silver-light) 0%, var(--silver-mid) 45%, var(--silver-dark) 70%, var(--silver-light) 100%);
    -webkit-background-clip: text;
    background-clip: text;
    color: transparent;
  }
  .cover__title span { display: block; }
  .cover__artist {
    position: absolute;
    left: 0;
    right: 0;
    top: 985px;
    text-align: center;
    font-weight: 600;
    font-size: 38px;
    color: var(--artist-white);
  }
  .cover__artist span {
    display: inline-block;
    padding-bottom: 4px;
    border-bottom: 3px solid var(--artist-white);
  }
</style>
</head>
<body>
  <main class="cover">
    <div class="cover__texture" role="img" aria-label="Dark charcoal geometric triangle pattern background"></div>
    <div class="cover__frame"></div>
    <h1 class="cover__title">
      <span>Turn</span>
      <span>The</span>
      <span>Lights</span>
      <span>Low</span>
    </h1>
    <p class="cover__artist"><span>DJ K</span></p>
  </main>
</body>
</html>
```